Steady Mind Coach website development

Need a website designed for a coaching business. Very high-end, luxury, professionalism, in the area of STRESS, see brief attached. I have a logo already
Updates

Slow in providing feedback

Target Market(s)

CEOs very successful men and wealthy females, high end luxury market

Industry/Entity Type

coaching

Number of Pages Required

1 page

Requirements
Must have
• Luxury look, professional, serious but warm, appealing to both sexes

```html
<!DOCTYPE html>
<html lang="en">
<head>
<meta charset="UTF-8">
<title>Steady Mind Coach</title>
<link href="https://fonts.googleapis.com/css2?family=Poppins:ital,wght@0,400;0,500;0,600;0,700;0,800;1,400&display=swap" rel="stylesheet">
<style>
:root{
  --mint:#93cbbc;
  --teal:#52a690;
  --teal-dark:#3f7f6c;
  --ink:#111;
  --body:#555;
  --soft:#f7f7f7;
  --orange:#ffad62;
  --coral:#fe8a7d;
  --star:#f5a55a;
  --btn:#5b5b5b;
}
*{margin:0;padding:0;box-sizing:border-box}
html,body{width:1200px;height:5037px;overflow:hidden}
body{position:relative;background:#fff;font-family:'Poppins',sans-serif;color:var(--body)}
.abs{position:absolute}
.brand{display:flex;align-items:center;gap:14px;font-weight:500;color:var(--ink);letter-spacing:6px}
.brand-mark{width:30px;height:30px;background:var(--ink)}
.nav a{position:absolute;top:21px;height:34px;line-height:34px;font-size:14px;color:#333;text-decoration:none;letter-spacing:.5px}
.nav .active{background:var(--teal-dark);color:#fff;padding:0 16px;left:592px;width:74px;text-align:center}
.hero-band{left:0;top:219px;width:1200px;height:523px;background:var(--mint)}
.hero-photo{left:637px;top:127px;width:479px;height:615px;background:linear-gradient(180deg,#9aa3a8,#4f5a63)}
.hero-title{left:154px;top:264px;font-size:54px;line-height:56px;font-weight:800;color:#fff}
.hero-text{left:154px;top:408px;width:410px;font-size:13px;line-height:31.5px;color:#fff}
.btn-light{left:154px;top:631px;width:159px;height:47px;background:#fff;color:var(--teal);font-size:13px;text-align:center;line-height:47px;letter-spacing:.5px}
.circle{border-radius:50%;width:332px;height:332px}
.quote{left:631px;top:996px;width:480px;font-size:13.5px;line-height:31.5px;font-style:italic;color:#222}
.quote p{margin-bottom:32px}
.welcome-title{left:0;top:1706px;width:1200px;text-align:center;font-size:29px;font-weight:600;color:var(--ink)}
.welcome-title span{color:var(--teal)}
.welcome-text{left:262px;top:1797px;width:676px;text-align:center;font-size:13.5px;line-height:31.8px}
.panel{top:2079px;height:449px}
.panel-title{top:2344px;font-size:50px;font-weight:800;color:#fff;text-align:center}
.panel-btn{top:2427px;width:158px;height:41px;line-height:41px;text-align:center;font-size:13px;color:#5a3c2c;background:rgba(255,255,255,.35)}
.why{left:0;top:2614px;width:1200px;height:565px;background:var(--teal);color:#fff;text-align:center}
.why h2{margin-top:150px;font-size:28px;font-weight:600}
.why p{width:880px;margin:0 auto;font-size:13.5px;line-height:31.5px;font-weight:500}
.benefits-title{left:0;top:3308px;width:1200px;text-align:center;font-size:29px;font-weight:600;color:var(--ink)}
.card{background:#fff;box-shadow:0 14px 40px rgba(0,0,0,.07);font-size:13.5px;line-height:31.5px;padding:0 58px;display:flex;align-items:center}
.stars{color:var(--star);font-size:30px;letter-spacing:14px}
.footer{left:0;top:4514px;width:1200px;height:441px;background:var(--soft)}
.footer h3{font-size:19px;font-weight:600;color:#333}
.footer .line{font-size:14px;line-height:32.5px;color:#555}
.social{width:30px;height:30px;border-radius:50%;background:#d4d4d4;top:4878px}
.field{left:825px;width:232px;height:33px;border:1.5px solid #999;background:#fff;font-size:13px;color:#777;padding:5px 14px}
.submit{left:825px;top:4866px;width:158px;height:44px;background:var(--btn);color:#fff;font-size:13px;font-weight:600;text-align:center;line-height:44px}
.copy{left:0;top:4975px;width:1200px;border-top:2px solid #777;text-align:center;font-size:13.5px;padding-top:16px;color:#555}
</style>
</head>
<body>

<header>
  <div class="abs brand" style="left:82px;top:66px;font-size:20px">
    <span class="brand-mark"></span>STEADY MIND COACH
  </div>
  <nav class="nav">
    <a class="active">HOME</a>
    <a style="left:710px">ABOUT US</a>
    <a style="left:832px">SERVICES</a>
    <a style="left:956px">BLOG</a>
    <a style="left:1045px">CONTACT</a>
  </nav>
</header>

<section class="hero">
  <div class="abs hero-band"></div>
  <div class="abs hero-photo" role="img" aria-label="Portrait of the head coach in a grey suit and red tie"></div>
  <h1 class="abs hero-title">HEAD COACH<br>GET IT!</h1>
  <p class="abs hero-text">Not your typical “quiet whale music playing in the background, kind of “stress guy”…stress is good, it can save your life…teach people to look at stress in a new light, to understand it, recognize when it is coming on, and decide to use it for performance, or control it…</p>
  <div class="abs btn-light">KNOW MORE</div>
</section>

<section class="mission">
  <div class="abs circle" style="left:170px;top:866px;background:var(--orange)" role="img" aria-label="Stressed man in a suit with clasped hands on an orange circle"></div>
  <div class="abs circle" style="left:170px;top:1208px;background:var(--coral)" role="img" aria-label="Worried man holding his head on a coral circle"></div>
  <div class="abs quote">
    <p>“ My desire is to help those in stress, recognize the signs of stress and how to channel the stress correctly.</p>
    <p>Provide techniques to reduce “bad” stress.</p>
    <p>My focus will be releasing stress and channeling it through wellness activities. Mindfulness, and knowing yourself, self-awareness.</p>
    <p>Not necessarily stress reduction but stress enhancement.</p>
    <p>I only have one job and that is to help clients think differently. Everything else is just fluff ”</p>
  </div>
</section>

<section class="welcome">
  <h2 class="abs welcome-title">WELCOME TO <span>STEADYMINDCOACH</span></h2>
  <p class="abs welcome-text">Steady Mind Coach came about due to my desire to help people lead a better and healthier life. Initially, I was involved in the fitness/body side of health. As years passed and my experience grew, I realized how important the mind was in total wellness, and that the mind is all powerful and controlling. Control the mind, control the body and achieve success. Stress can be the most debilitating factor in our lives, it is the root cause of so many diseases and costs the US workplace an estimated 300 billion dollars due to loss of productivity.</p>
</section>

<section class="audience">
  <div class="abs panel" style="left:0;width:592px;background:linear-gradient(135deg,#e9b98a,#f5d7b4 55%,#d9a676)" role="img" aria-label="Smiling man working at a laptop, warm orange tint"></div>
  <div class="abs panel" style="left:608px;width:592px;background:linear-gradient(135deg,#efb7b4,#f6cdca 55%,#e3a8a6)" role="img" aria-label="Smiling woman with a mug at a laptop, soft pink tint"></div>
  <div class="abs panel-title" style="left:0;width:592px">FOR MEN</div>
  <div class="abs panel-title" style="left:608px;width:592px">FOR WOMEN</div>
  <div class="abs panel-btn" style="left:217px">CLICK HERE</div>
  <div class="abs panel-btn" style="left:825px">CLICK HERE</div>
</section>

<section class="abs why">
  <h2>WHY ME ?</h2>
  <p style="margin-top:46px">• Been there done that! Have been through a lot, started businesses, selling a business, law suits, marriage, divorce, second marriage, kids, school, sports, fights, robbed, gun in face, traveled the world, successful, two great kids (both Cadets at Ridgeview Academy…duty/honor/country)</p>
  <p style="margin-top:32px">• Limited number of clients…different stage of life, empty nester, have a full career…won’t be a number</p>
</section>

<section class="benefits">
  <h2 class="abs benefits-title">BENEFITS</h2>
  <div class="abs card" style="left:344px;top:3423px;width:508px;height:178px;flex-direction:column;justify-content:center">
    <div class="stars">★★★★★</div>
    <div style="margin-top:6px">• Experience</div>
  </div>
  <div class="abs card" style="left:82px;top:3693px;width:508px;height:297px">• Sector expert Health/Wellness. Presented at numerous industry shows and quoted in national publications (not as a coach, I’m new, but in the health &amp; wellness space)</div>
  <div class="abs card" style="left:608px;top:3693px;width:508px;height:297px">• Excellent listener…being in sales for many years, the secret is to really listen…and get to the end game, and make it feel as if it was their decision. Not sure how to word this as a benefit.</div>
  <div class="abs card" style="left:82px;top:4068px;width:508px;height:309px">• Access/resources industry professionals, sport psychologist…just spent a few hours with the Mind performance coach for the Harbor City Hawks baseball team…I can get the best advice and latest techniques in mind/body training performance.</div>
  <div class="abs card" style="left:608px;top:4068px;width:508px;height:309px">• Private, more than happy to sign confidentiality agreement. Especially for the business man.</div>
</section>

<footer>
  <div class="abs footer"></div>
  <div class="abs brand" style="left:82px;top:4620px;font-size:13px;letter-spacing:4px;gap:10px">
    <span class="brand-mark" style="width:20px;height:20px"></span>STEADY MIND COACH
  </div>
  <div class="abs line" style="left:82px;top:4674px" >Linden Row, Harbor<br>Main Street USA<br>hello@steadymindcoach.com<br>002-555014720</div>
  <div class="abs" style="left:82px;top:4837px;font-size:19px;font-weight:600;color:#333">Follow Us</div>
  <div class="abs social" style="left:83px"></div>
  <div class="abs social" style="left:120px"></div>
  <div class="abs social" style="left:159px"></div>
  <div class="abs social" style="left:196px"></div>

  <div class="abs" style="left:483px;top:4590px"><h3>Quick Links</h3></div>
  <div class="abs line" style="left:483px;top:4620px">Home<br>About us<br>Blog<br>Services</div>

  <div class="abs" style="left:825px;top:4586px"><h3>Contact us</h3></div>
  <div class="abs field" style="top:4633px">Name</div>
  <div class="abs field" style="top:4674px">E-Mail</div>
  <div class="abs field" style="top:4715px">Subject</div>
  <div class="abs field" style="top:4758px;height:84px">Message</div>
  <div class="abs submit">SUBMIT</div>

  <div class="abs copy">Copyright @ 2022 all right reserved.</div>
</footer>

</body>
</html>
```